Radiant Crossing - An Exciting Mission & Book Cover Project

Help me to inspire people to live their best life! This is a mission, not just a design project.
I need a Book Cover designed to keep me inspired on the process of writing my book.
Book Title: Radiant Crossing
Tag Line: Three Simple Steps to get out of your own way, SuperCharge your Life and Step into Purpose!
Author: Marlis Quenby

The three steps are: Ownership, Vision and Action (Not sure if this should be on the front or back of the book cover)

The book is a self-help, motivational book. Personal development.
The cover needs to be strong and capture peoples attention, especially with competing shelf space. I almost see a fire ball of flame or explosion that will grab peoples attention.
My company is The Lantern Institute. I have added the company logo and a few pages of my presentation and topic outline to give an idea.
Maybe: The Lantern Institute logo on back of the cover. website is marlisquenby.com

THOUGHT: People should be able to take a photo of them holding the book cover showing what area of life they want Radiant Crossing in. This is why the front cover must be so visual and powerful that they want to take a photo with it. Ie. Explosion, fire, strong and bold.

Target Market(s)

Anyone who feels stuck and needs to breakthrough and move forward in life.

Industry/Entity Type

Motivation

Font styles to use
Serif
Sans Serif

Colors
ec1f27
f37122
fbed22

Requirements
Must have
• The design must be STRONG, SIMPLE, STAND OUT ON BOOK SHELVES.
Must have an open file to swap the photo and copy out.

Back Cover Page
1) Summary
2) 2-3 testimonials. One sentence.
3) About the Author (maybe with photo)
4) Lantern Institute logo
5) Website: radiantcrossing.com and marlisquenby.com
Nice to have
• If my photo works somewhere that would be great. I will change the photo later.
Added Where's Your Harbor? a nice cover example.
Should not have
• Right now I am writing the summary for the back of the cover. For now use Loreum Ipsum text and 2-3 recommendations. Again, I will get these only later.

```html
<!DOCTYPE html>
<html lang="en">
<head>
<meta charset="utf-8">
<title>Radiant Crossing – Cover Spread</title>
<link href="https://fonts.googleapis.com/css2?family=Oswald:wght@400;500;600;700&family=Open+Sans:wght@400;600;700&display=swap" rel="stylesheet">
<style>
  :root{
    --ink:#050505;
    --paper:#ffffff;
    --flame-red:#ec1f27;
    --flame-orange:#f37122;
    --flame-yellow:#fbed22;
    --body-text:#d8d8d8;
    --muted:#9a9a9a;
  }
  *{margin:0;padding:0;box-sizing:border-box}
  html,body{width:745px;height:1200px;overflow:hidden;background:var(--paper)}
  .canvas{position:relative;width:745px;height:1200px;background:var(--paper)}
  .spread{position:absolute;left:0;top:232px;width:745px;height:736px;display:flex;background:var(--ink)}

  /* back cover */
  .back{position:relative;width:340px;height:100%;padding:34px 30px 0 30px;font-family:"Open Sans",sans-serif;color:var(--body-text)}
  .brand{display:flex;align-items:center;gap:8px;margin-bottom:30px}
  .brand-dot{width:16px;height:16px;border-radius:50%;background:var(--flame-orange)}
  .brand-name{font-family:"Open Sans",sans-serif;font-weight:600;font-size:11px;color:var(--paper);letter-spacing:.5px;text-transform:uppercase}
  .summary p{font-size:10.5px;line-height:1.55;margin-bottom:14px}
  .author-block{position:absolute;left:30px;right:24px;bottom:36px;display:flex;gap:14px;align-items:flex-start}
  .author-photo{width:110px;height:150px;flex:none;background:linear-gradient(180deg,#2a2f3a 0%,#1a2030 55%,#0c0f16 100%)}
  .author-bio{font-size:9.5px;line-height:1.5;padding-top:8px}
  .author-bio strong{color:var(--paper)}
  .author-links{margin-top:12px;color:var(--paper);font-size:9.5px;line-height:1.5}

  /* spine */
  .spine{position:relative;width:56px;height:100%;display:flex;flex-direction:column;align-items:center;padding-top:20px;border-left:1px solid #151515;border-right:1px solid #151515}
  .spine-mark{width:12px;height:12px;border-radius:50%;background:var(--flame-orange)}
  .spine-text{writing-mode:vertical-rl;font-family:"Oswald",sans-serif;text-transform:uppercase;margin-top:26px}
  .spine-title{font-size:30px;font-weight:600;letter-spacing:1px;background:linear-gradient(90deg,var(--flame-yellow),var(--flame-orange) 55%,var(--flame-red));-webkit-background-clip:text;background-clip:text;color:transparent}
  .spine-author{font-size:13px;font-weight:500;color:var(--paper);letter-spacing:3px;margin-top:54px}

  /* front cover */
  .front{position:relative;width:349px;height:100%;overflow:hidden}
  .flame-art{position:absolute;left:70px;top:250px;width:279px;height:486px;background:radial-gradient(ellipse at 60% 55%,#fbed22 0%,#f37122 22%,#c2401a 42%,#3a1208 68%,rgba(5,5,5,0) 85%)}
  .tagline{position:absolute;left:30px;right:30px;top:34px;text-align:center;font-family:"Oswald",sans-serif;font-weight:500;font-size:16px;line-height:1.3;color:var(--flame-orange);text-transform:uppercase;letter-spacing:.3px}
  .title{position:absolute;left:0;right:0;top:112px;text-align:center;font-family:"Oswald",sans-serif;font-weight:700;text-transform:uppercase;line-height:1.02;background:linear-gradient(180deg,var(--flame-yellow) 0%,var(--flame-orange) 60%,var(--flame-red) 100%);-webkit-background-clip:text;background-clip:text;color:transparent}
  .title-line-1{display:block;font-size:56px;letter-spacing:1px}
  .title-line-2{display:block;font-size:44px;letter-spacing:.5px}
  .front-author{position:absolute;left:26px;bottom:40px;font-family:"Oswald",sans-serif;font-weight:700;font-size:30px;line-height:1.05;color:var(--paper);text-transform:uppercase}
</style>
</head>
<body>
<main class="canvas">
  <section class="spread">
    <article class="back">
      <div class="brand"><span class="brand-dot"></span><span class="brand-name">The Lantern Institute</span></div>
      <div class="summary">
        <p>Lorem ipsum dolor sit amet, ut iriure pertinax incorrupte. Cum illum omnes scriptorem in, mel ne dicit partiendo. Sea detracto definitionem cu, tempor utinam tractatos per et.</p>
        <p>Ius probo malorum sensibus ei. Soluta mentitum vulputate pri an, eu duo consul tincidunt. Nam in iusto mollis maiorum, mazim ullamcorper vim et.</p>
        <p>In mucius delicatissimi ius. Et atqui eloquentiam quo, at atqui tincidunt sea. Ex dolorem consetetur duo, nam prompta scripserit voluptatibus.</p>
        <p>Augue deleniti ius ne, an mel primis efficiendi. Usu an audire legimus, eos invenire molestiae no.</p>
      </div>
      <div class="author-block">
        <div class="author-photo" role="img" aria-label="Portrait photograph of the author in a dark suit"></div>
        <div class="author-bio">
          <p><strong>Marlis Quenby</strong> Lorem ipsum dolor sit amet, vim id iriure pertinax incorrupte. Cum illum omnes scriptorem ut, mel ne dicit partiendo. Sea detracto definitionem cu, tempor utinam tractatos his ut.</p>
          <p class="author-links">marlisquenby.com<br>radiantcrossing.com</p>
        </div>
      </div>
    </article>

    <aside class="spine">
      <span class="spine-mark"></span>
      <div class="spine-text">
        <span class="spine-title">Radiant Crossing</span>
        <span class="spine-author">Marlis Quenby</span>
      </div>
    </aside>

    <article class="front">
      <div class="flame-art" role="img" aria-label="Raised fist bursting through a blaze of fire and sparks"></div>
      <p class="tagline">Three simple steps to get out of your own way, supercharge your life and step into purpose!</p>
      <h1 class="title"><span class="title-line-1">Radiant</span><span class="title-line-2">Crossing</span></h1>
      <p class="front-author">Marlis<br>Quenby</p>
    </article>
  </section>
</main>
</body>
</html>
```